Cleaning service website design

We need a new nice web design(logo will be the same) for a new cleaning service Company:

Informations about Company and logo you can take from flyers in attachments.

This is a cleaning service Company which have simple rules and we would like to show that(in checklist form) on website:

- What we do and that we're Cleaning Green

- Why us?

- How much(our pricing is simple)

Also we would like to communicate with clients by some nice/big pictures on website and the most important thing is our phone number and short/fast Freestimate.

Also there should be some space for description about our Company.

Generally all information on main page can be short: about us, about service(what we do), last reviews, tips (for example: Tip of the week) and other can be some introduction to subpage where will be more information.

There will be few subpages like: About us, About our service, Photos(Before and after), Reviews , Tips, FAQ, Contact, Looking for a Job? - most of them will be just text so you can project just one example.

```html
<!DOCTYPE html>
<html lang="en">
<head>
<meta charset="utf-8">
<title>Tidy Nest House Cleaning</title>
<link href="https://fonts.googleapis.com/css2?family=Open+Sans:wght@300;400;600;700;800&family=Yanone+Kaffeesatz:wght@400&family=PT+Sans+Narrow:wght@700&display=swap" rel="stylesheet">
<style>
:root{
  --green:#6db41c;
  --green-dark:#3f7d18;
  --navy:#1d4f8c;
  --orange:#f07d12;
  --orange-light:#fbab2a;
  --text:#2b2b2b;
  --muted:#888;
  --line:#d6d6d6;
  --footer:#2a2a2a;
  --footer-bottom:#1b1b1b;
  --white:#fff;
  --red:#d71d1d;
}
*{margin:0;padding:0;box-sizing:border-box}
html,body{width:800px;height:1200px;overflow:hidden;background:var(--white)}
body{font-family:"Open Sans",Arial,sans-serif;color:var(--text)}
.canvas{position:relative;width:800px;height:1200px;overflow:hidden}
.abs{position:absolute}

/* header */
.site-header{position:absolute;left:0;top:0;width:800px;height:86px;border-bottom:2px solid #e4e4e4;background:var(--white)}
.brand{position:absolute;left:100px;top:24px;display:flex;align-items:center;gap:6px}
.brand-dot{width:22px;height:22px;border-radius:50%;background:var(--navy)}
.brand-name{font-size:22px;font-weight:700;color:var(--green-dark);line-height:1}
.brand-sub{position:absolute;left:124px;top:66px;font-size:7px;font-weight:600;color:var(--navy)}
.call{position:absolute;right:100px;top:9px;text-align:right}
.call-label{font-size:8px;color:var(--text)}
.call-label b{font-weight:700}
.call-number{display:flex;align-items:center;justify-content:flex-end;gap:4px;font-size:16px;font-weight:800;color:#111;margin-top:1px}
.main-nav{position:absolute;right:100px;top:44px;display:flex;height:42px}
.main-nav a{font-family:"PT Sans Narrow",sans-serif;font-weight:700;font-size:8.5px;color:#222;text-decoration:none;padding:15px 10px 0;height:42px;letter-spacing:.2px}
.main-nav a.active{background:#efefef;color:var(--green);border-bottom:3px solid var(--green)}
.main-nav a:last-child{padding-right:0}

/* hero */
.hero{position:absolute;left:0;top:89px;width:800px;height:335px;background:radial-gradient(ellipse at 65% 30%,#a9cd5a 0%,#6ea02a 35%,#3b6e16 70%,#2a5411 100%)}
.hero-photo{position:absolute;left:420px;top:30px;width:300px;height:305px;background:linear-gradient(160deg,rgba(170,180,90,.55),rgba(120,140,50,.35));border-radius:140px 140px 0 0}
.hero-title{position:absolute;left:100px;top:122px;font-size:27px;font-weight:300;color:var(--white);letter-spacing:.3px}
.hero-title b{font-weight:700}
.hero-sub{position:absolute;left:100px;top:156px;font-size:14px;font-weight:600;color:var(--white)}
.hero-sub .price{color:var(--red);font-size:24px;font-weight:700;vertical-align:-2px}
.perks{position:absolute;left:100px;top:192px;list-style:none}
.perks li{display:flex;align-items:center;gap:8px;height:22.3px;font-size:9.5px;color:var(--white)}
.badge{position:absolute;left:207px;top:271px;width:48px;height:48px;border-radius:50%;background:radial-gradient(circle at 40% 35%,#ffffff,#c9e7a5 60%,#7dbb33)}
.cta{position:absolute;left:100px;top:340px;width:164px;height:38px;border-radius:3px;background:linear-gradient(#ffa92b,#f07b0c);display:flex;align-items:center;justify-content:center;gap:8px;color:var(--white);font-size:16px;font-weight:700;text-decoration:none}

/* cards */
.card{position:absolute;top:450px;width:191px;height:227px;border:1px solid var(--line);background:var(--white);box-shadow:0 6px 6px -5px rgba(0,0,0,.18)}
.card-photo{position:absolute;left:3px;top:3px;width:183px;height:72px}
.card h2{position:absolute;left:0;top:81px;width:100%;text-align:center;font-size:12.5px;font-weight:600;color:var(--green)}
.checks{position:absolute;left:14px;top:107px;list-style:none;width:170px}
.checks li{display:flex;gap:6px;font-size:8.5px;line-height:12.5px;margin-bottom:6px}
.checks svg{flex:none;margin-top:1px}
.prices{position:absolute;left:22px;top:107px;list-style:none;font-size:8.5px}
.prices li{margin-bottom:5.5px}
.prices b{color:var(--green-dark);font-weight:600}
.price-note{position:absolute;left:24px;top:166px;width:160px;font-size:8px;line-height:11.5px}
.price-note a{color:var(--navy)}
.rates{position:absolute;left:25px;top:198px;font-size:6.5px;font-style:italic}

.estimate h2{top:15px;font-size:13px}
.field{position:absolute;left:19px;height:19px;border:1px solid #cfcfcf;font-size:6.5px;color:var(--muted);padding:5px 0 0 7px}
.est-call{position:absolute;left:20px;top:186px;font-size:7px;font-weight:700}
.est-call span{display:block;font-size:13px;font-weight:700;color:var(--navy);margin-top:-2px}
.submit{position:absolute;left:115px;top:186px;width:56px;height:17px;background:linear-gradient(#ff8a1a,#e4640a);color:var(--white);font-size:7.5px;font-weight:700;display:flex;align-items:center;justify-content:center}

/* about */
.about{position:absolute;left:100px;top:707px;width:600px;height:94px;border:1px solid var(--line)}
.about-photo{position:absolute;left:101px;top:694px;width:148px;height:107px;background:linear-gradient(#cfd3d8,#8a929c);border-radius:60px 60px 0 0}
.about h2{position:absolute;left:155px;top:14px;font-family:"Yanone Kaffeesatz",sans-serif;font-weight:400;font-size:22px;color:var(--green)}
.about p{position:absolute;left:155px;top:40px;width:430px;font-size:7.6px;line-height:12.5px}
.read-more{position:absolute;right:14px;top:70px;font-size:6.5px;font-weight:600;color:var(--green-dark)}

/* review & tip */
.panel{position:absolute;left:100px;top:827px;width:600px;height:166px;border:1px solid var(--line)}
.panel-title{position:absolute;font-size:12.5px;font-weight:600;color:var(--green)}
.review-photo{position:absolute;left:12px;top:60px;width:92px;height:105px;background:linear-gradient(#e8d6c2,#3a3a3a 65%);border-radius:40px 40px 0 0}
.bubble{position:absolute;left:88px;top:38px;width:234px;height:85px;border:1px solid #d2d2d2;border-radius:4px;background:#fafafa;padding:8px 10px}
.bubble-head{font-size:8px;font-weight:700}
.bubble-head span{font-weight:400;color:var(--muted);font-size:7px;margin-left:12px}
.bubble p{font-size:8px;font-style:italic;line-height:12.5px;margin-top:4px;color:#444}
.bubble-meta{display:flex;gap:8px;align-items:center;font-size:6.5px;border-top:1px dotted #bbb;margin-top:4px;padding-top:3px}
.bubble-meta .stars{color:var(--red);font-size:8px;letter-spacing:-1px}
.bubble-meta a{color:var(--navy)}
.btn-more{position:absolute;width:62px;height:16px;background:var(--green-dark);color:var(--white);font-size:7px;display:flex;align-items:center;justify-content:center;border:1px solid #2e6010}
.divider{position:absolute;left:361px;top:44px;width:1px;height:94px;background:var(--line)}
.tip-link{position:absolute;left:384px;top:50px;font-size:9px;font-weight:600;color:var(--navy);text-decoration:underline}
.tip-text{position:absolute;left:384px;top:66px;width:190px;font-size:7.5px;line-height:12.5px}

/* footer */
.site-footer{position:absolute;left:0;top:1017px;width:800px;height:156px;background:var(--footer);color:var(--white)}
.foot-col{position:absolute;top:26px}
.foot-col h3{font-size:10.5px;font-weight:600;margin-bottom:7px}
.foot-col a{display:block;font-size:7.5px;color:var(--white);text-decoration:none;line-height:15.7px}
.foot-col p{font-size:7.5px;margin-bottom:8px}
.news-input{width:204px;height:26px;background:var(--white);color:#222;font-size:7.5px;padding:8px 10px;display:inline-block;vertical-align:top}
.news-go{display:inline-block;width:28px;height:26px;margin-left:4px;background:linear-gradient(#ffb23a,#f08a10);font-size:9px;font-weight:700;text-align:center;line-height:26px}
.social{position:absolute;left:463px;top:114px;display:flex;gap:4px}
.social span{width:16px;height:16px;border-radius:2px}
.foot-brand{position:absolute;left:618px;top:122px;display:flex;align-items:center;gap:5px}
.foot-brand .brand-dot{width:16px;height:16px}
.foot-brand .brand-name{font-size:15px;color:var(--green)}
.foot-bottom{position:absolute;left:0;top:1173px;width:800px;height:27px;background:var(--footer-bottom);font-size:7px;color:#555;padding:10px 100px}
</style>
</head>
<body>
<div class="canvas">

  <header class="site-header">
    <div class="brand"><span class="brand-dot"></span><span class="brand-name">Tidy Nest</span></div>
    <div class="brand-sub">House Cleaning</div>
    <div class="call">
      <div class="call-label"><b>Call Us</b> to arrange your cleaning on</div>
      <div class="call-number">
        <svg width="11" height="13" viewBox="0 0 24 24" aria-hidden="true"><path fill="#1d4f8c" d="M6.6 10.8a15 15 0 0 0 6.6 6.6l2.2-2.2c.3-.3.7-.4 1-.2 1.1.4 2.3.6 3.6.6.6 0 1 .4 1 1V20c0 .6-.4 1-1 1A17 17 0 0 1 3 4c0-.6.4-1 1-1h3.5c.6 0 1 .4 1 1 0 1.3.2 2.5.6 3.6.1.3 0 .7-.2 1z"/></svg>
        555-014-2290
      </div>
    </div>
    <nav class="main-nav">
      <a class="active" href="#">HOME</a><a href="#">ABOUT US</a><a href="#">OUR SERVICES</a><a href="#">PHOTOS</a><a href="#">REVIEWS</a><a href="#">TIPS</a><a href="#">CAREERS</a><a href="#">FAQ</a><a href="#">CONTACT</a>
    </nav>
  </header>

  <section class="hero" role="img" aria-label="Photo of a carefree woman stretching her arms in a sunny green meadow">
    <div class="hero-photo"></div>
  </section>
  <h1 class="hero-title">SIMPLIFY <b>YOUR LIFE</b></h1>
  <p class="hero-sub">and some there House Cleaning from <span class="price">$79</span></p>
  <ul class="perks">
    <li><svg width="12" height="12" viewBox="0 0 12 12" aria-hidden="true"><path d="M2 6.5l2.5 2.5L10 3" stroke="#9ed94a" stroke-width="2" fill="none"/></svg>Locally Owned &amp; Operated</li>
    <li><svg width="12" height="12" viewBox="0 0 12 12" aria-hidden="true"><path d="M2 6.5l2.5 2.5L10 3" stroke="#9ed94a" stroke-width="2" fill="none"/></svg>Reliable &amp; Affordable</li>
    <li><svg width="12" height="12" viewBox="0 0 12 12" aria-hidden="true"><path d="M2 6.5l2.5 2.5L10 3" stroke="#9ed94a" stroke-width="2" fill="none"/></svg>All Supplies Provided</li>
    <li><svg width="12" height="12" viewBox="0 0 12 12" aria-hidden="true"><path d="M2 6.5l2.5 2.5L10 3" stroke="#9ed94a" stroke-width="2" fill="none"/></svg>No Contracts</li>
    <li><svg width="12" height="12" viewBox="0 0 12 12" aria-hidden="true"><path d="M2 6.5l2.5 2.5L10 3" stroke="#9ed94a" stroke-width="2" fill="none"/></svg>Pet Friendly</li>
    <li><svg width="12" height="12" viewBox="0 0 12 12" aria-hidden="true"><path d="M2 6.5l2.5 2.5L10 3" stroke="#9ed94a" stroke-width="2" fill="none"/></svg>Green Cleaning</li>
  </ul>
  <div class="badge" role="img" aria-label="Green cleaning badge"></div>
  <a class="cta" href="#">GET STARTED
    <svg width="18" height="16" viewBox="0 0 18 16" aria-hidden="true"><path d="M1 5h9V1l7 7-7 7v-4H1z" fill="#fff"/></svg>
  </a>

  <article class="card" style="left:100px">
    <div class="card-photo" role="img" aria-label="Photo of a smiling family with their dog on a sofa" style="background:linear-gradient(90deg,#c9a47a,#e7d1b4 50%,#a4896a)"></div>
    <h2>What do we clean?</h2>
    <ul class="checks">
      <li><svg width="11" height="11" viewBox="0 0 11 11" aria-hidden="true"><rect x=".5" y="1.5" width="9" height="9" fill="none" stroke="#3f7d18"/><path d="M2.5 5.5l2 2L10 1" stroke="#3f7d18" stroke-width="1.6" fill="none"/></svg>Thoroughly clean your bathrooms, kitchen, bedrooms and living areas</li>
      <li><svg width="11" height="11" viewBox="0 0 11 11" aria-hidden="true"><rect x=".5" y="1.5" width="9" height="9" fill="none" stroke="#3f7d18"/><path d="M2.5 5.5l2 2L10 1" stroke="#3f7d18" stroke-width="1.6" fill="none"/></svg>Mop or vacuum your floors</li>
      <li><svg width="11" height="11" viewBox="0 0 11 11" aria-hidden="true"><rect x=".5" y="1.5" width="9" height="9" fill="none" stroke="#3f7d18"/><path d="M2.5 5.5l2 2L10 1" stroke="#3f7d18" stroke-width="1.6" fill="none"/></svg>Dust surfaces</li>
      <li><svg width="11" height="11" viewBox="0 0 11 11" aria-hidden="true"><rect x=".5" y="1.5" width="9" height="9" fill="none" stroke="#3f7d18"/><path d="M2.5 5.5l2 2L10 1" stroke="#3f7d18" stroke-width="1.6" fill="none"/></svg>Collect garbage</li>
      <li><svg width="11" height="11" viewBox="0 0 11 11" aria-hidden="true"><rect x=".5" y="1.5" width="9" height="9" fill="none" stroke="#3f7d18"/><path d="M2.5 5.5l2 2L10 1" stroke="#3f7d18" stroke-width="1.6" fill="none"/></svg>Make beds</li>
    </ul>
  </article>

  <article class="card" style="left:304px">
    <div class="card-photo" role="img" aria-label="Photo of a happy family looking at a laptop" style="background:linear-gradient(90deg,#e9e0d2,#d9b896 50%,#cfd6dc)"></div>
    <h2>Pricing is..simple</h2>
    <ul class="prices">
      <li><b>$79</b> for homes less than 1000 sq ft</li>
      <li><b>$89</b> for homes 1000-1800 sq ft</li>
      <li><b>$99</b> for homes 1800-2600 sq ft</li>
    </ul>
    <p class="price-note">If your home is larger than 2600 sq ft please <a href="#">call for a quote</a></p>
    <p class="rates">*rates are for regular service*</p>
  </article>

  <aside class="card estimate" style="left:508px">
    <h2>Quick Free Estimate</h2>
    <div class="field" style="top:38px;width:149px">Name</div>
    <div class="field" style="top:66px;width:149px">E-mail</div>
    <div class="field" style="top:94px;width:149px">Postal Code</div>
    <div class="field" style="top:122px;width:149px">Phone</div>
    <div class="field" style="top:150px;width:73px">No. of Bathrooms</div>
    <div class="field" style="left:96px;top:150px;width:72px">No. of Bedrooms</div>
    <div class="est-call">CALL US TODAY<span>555-014-2290</span></div>
    <div class="submit">SUBMIT</div>
  </aside>

  <section class="about">
    <h2>About TidyNest.com</h2>
    <p>It's about caring, not just cleaning. Having personally experienced the struggles of finding quality maid service for our home, we want to make it simpler for families in the Oakridge area. Our goal is to provide caring, consistent and reliable house cleaning to every customer we serve.</p>
    <span class="read-more">READ MORE...</span>
  </section>
  <div class="about-photo" role="img" aria-label="Photo of the two company founders"></div>

  <section class="panel">
    <h2 class="panel-title" style="left:18px;top:14px">Featured Review</h2>
    <div class="review-photo" role="img" aria-label="Photo of a smiling customer in a business suit"></div>
    <div class="bubble">
      <div class="bubble-head">Dana Reyes, Oakridge <span>1 review</span></div>
      <p>I had to move out of a rental property and didn't want to hassle with the cleaning, so I called Tidy Nest whom quoted me over the phone and did a brilliant job.</p>
      <div class="bubble-meta"><span class="stars">★★★★★</span><span>09/07/2013</span><a>COMMENT</a><a>REPORT</a><a>Share</a><span>HELPFUL?</span></div>
    </div>
    <div class="btn-more" style="left:260px;top:137px">View more &gt;</div>

    <div class="divider"></div>
    <h2 class="panel-title" style="left:384px;top:14px">Tip of the Week</h2>
    <a class="tip-link" href="#">Cleaning up after your dog or cat</a>
    <p class="tip-text">For millions of dog and cat owners, Fido and Fluffy aren't just pets – they're part of the family.<br>But as much as we love our four-legged friends, they sure can .....</p>
    <div class="btn-more" style="left:511px;top:137px">View more &gt;</div>
  </section>

  <footer class="site-footer">
    <div class="foot-col" style="left:100px"><h3>Quick Links</h3><a>Home</a><a>About Us</a><a>Our Service</a><a>Photos</a><a>Contact</a></div>
    <div class="foot-col" style="left:220px"><h3>Useful Links</h3><a>Terms of use</a><a>Privacy Policy</a><a>Help Center</a><a>Community</a><a>Login Area</a></div>
    <div class="foot-col" style="left:328px"><h3>Join Our Community</h3><a>Friendbook</a><a>Chirper</a><a>WorkLinks</a></div>
    <div class="foot-col" style="left:463px"><h3>SignUp For Our Monthly Newsletter</h3><p>Subscribe our newsletter &amp; get the latest news &amp; updates</p><span class="news-input">Email Address</span><span class="news-go">GO</span></div>
    <div class="social"><span style="background:#2f5fa8"></span><span style="background:#3ba7dc"></span><span style="background:#f0a21e"></span></div>
    <div class="foot-brand"><span class="brand-dot"></span><span class="brand-name">Tidy Nest</span></div>
  </footer>
  <div class="foot-bottom">© 2013 by, Tidy Nest. All Rights Reserved.</div>

</div>
</body>
</html>
```